New, modern business card for growing audiology practice

We need a new business card for our audiology practice. Our logo and website have recently changed (more modern) and we want our business cards to reflect this change.
We conduct hearing tests, perform earwax removals, and fit & dispense hearing aids to our patients. We are a family owned practice in which the owner is the one who works directly with the patient. I have attached logos in various formats to use, as well as two ideas I found on this website; as well as a scanned copy of our current logo. Good luck!

Industry/Entity Type

Business

Contact Information for Business Card

Company name: Maplow Hearing Center
Provider name: Peter Mulvoy, Au.D. F/ISN
Phone number: (555) 318-6042
Address: 87 W. Linden Ave. Alder Falls, OH 43910
email: maplowhearing@postvale.net
website: maplowhearing.com

Colors
000000
aaaaaa
dbdbdb
cacaca
9bcb3c
afd23c
cadf82
b1b1b1

Requirements
Must have
• My card must include information in the "details" section. In the attached images, I found a few that I liked and I would like to model after - "brisk tumblin'" and "Sound Wellness Center".
• Must be horizontal.
• Must include logos provided. I uploaded them in various file formats and various ways.
• Must match logo font, if possible, if not, please get as close as you can.
Nice to have
• I really like the idea of having a color on one side with just the logo and company name and the contact information and provider name on the other side. I also really like the idea of having the main color dominating on the logo/company side with accent of that same color on the contact side of the card.
Should not have
• Must not be vertical.

```html
<!DOCTYPE html>
<html lang="en">
<head>
<meta charset="utf-8">
<title>Maplow Hearing Center – Business Card</title>
<link rel="stylesheet" href="https://fonts.googleapis.com/css2?family=Lato:wght@400&family=Roboto:wght@400;500&family=Roboto+Condensed:wght@700&display=swap">
<style>
  :root {
    --backdrop: #e6e6e6;
    --card-white: #f4f4f4;
    --card-black: #000000;
    --brand-green: #6fa237;
    --ink: #111111;
    --ink-soft: #444444;
    --rule: #555555;
    --white: #ffffff;
  }
  * { margin: 0; padding: 0; box-sizing: border-box; }
  html, body { width: 1200px; height: 960px; overflow: hidden; }
  body { background: var(--backdrop); position: relative; font-family: "Roboto", Arial, sans-serif; }

  .card { position: absolute; width: 600px; box-shadow: 0 3px 8px rgba(0,0,0,.35); }

  .card-front { left: 314px; top: 113px; height: 342px; background: var(--card-white); }
  .card-back  { left: 311px; top: 472px; height: 343px; background: var(--card-black); }

  .brand-name {
    position: absolute; display: flex; align-items: center; gap: 10px;
    font-family: "Lato", "Gill Sans", sans-serif; font-weight: 400;
    letter-spacing: 0.2px; white-space: nowrap;
  }
  .brand-dot { width: 16px; height: 16px; border-radius: 50%; background: var(--brand-green); flex: none; }

  .card-front .brand-name { right: 30px; top: 50px; font-size: 26px; color: var(--ink); }
  .card-back .brand-name { left: 0; right: 0; top: 156px; justify-content: center; font-size: 29px; color: var(--white); }

  .provider-name {
    position: absolute; left: 28px; top: 192px;
    font-family: "Roboto Condensed", Arial, sans-serif; font-weight: 700;
    font-size: 22px; color: var(--brand-green); text-transform: uppercase;
  }
  .provider-title {
    position: absolute; left: 28px; top: 220px;
    font-weight: 500; font-size: 14px; color: var(--ink); letter-spacing: 0.3px;
  }
  .divider { position: absolute; left: 28px; width: 543px; top: 246px; height: 0; border-top: 1.5px solid var(--rule); }

  .contact-list { position: absolute; left: 28px; top: 261px; list-style: none; }
  .contact-list li { display: flex; align-items: center; gap: 8px; height: 19px; font-size: 14px; color: var(--ink-soft); }
  .contact-list svg { width: 13px; height: 13px; fill: var(--brand-green); flex: none; }

  .address { position: absolute; right: 28px; top: 280px; text-align: right; font-size: 14px; line-height: 19px; color: var(--ink-soft); font-style: normal; }

  .card-bands { position: absolute; left: 0; bottom: 0; width: 600px; height: 8px; display: block; }

  .site-url {
    position: absolute; left: 0; right: 0; top: 287px; text-align: center;
    font-size: 14px; letter-spacing: 3.2px; color: var(--white);
  }
  .site-url .accent { color: var(--brand-green); }
</style>
</head>
<body>

<section class="card card-front" aria-label="Business card front">
  <div class="brand-name"><span class="brand-dot"></span>MAPLOW HEARING CENTER</div>

  <h1 class="provider-name">Peter Mulvoy</h1>
  <p class="provider-title">AU.D. F/ISN</p>
  <div class="divider"></div>

  <ul class="contact-list">
    <li>
      <svg viewBox="0 0 16 16" aria-hidden="true"><path d="M3.6 1.2l2.2 2.9c.3.4.2.9-.1 1.2L4.5 6.5c.9 2 2.6 3.9 4.9 5l1.2-1.2c.3-.3.9-.4 1.2-.1l2.9 2.2c.4.3.4.8.1 1.2l-1.4 1.4c-.6.6-1.6.8-2.4.4C6.2 13.5 2.5 9.8.7 5c-.3-.8-.1-1.8.5-2.4l1.2-1.3c.3-.4.9-.4 1.2-.1z"/></svg>
      (555) 318-6042
    </li>
    <li>
      <svg viewBox="0 0 16 16" aria-hidden="true"><path d="M1 3.5h14v1L8 9 1 4.5z"/><path d="M1 6l7 4.5L15 6v6.5H1z"/></svg>
      maplowhearing@postvale.net
    </li>
    <li>
      <svg viewBox="0 0 16 16" aria-hidden="true"><circle cx="8" cy="8" r="7"/><path d="M4 5c1 0 2 .5 2.5 1.5S6 8.5 5 9 4 11 4.5 12.5 M10 3c.5 1 0 2 1 2.5s2 0 2.5 1 M11 10c-.5 1 0 2 .5 3" stroke="#f4f4f4" stroke-width="1.3" fill="none"/></svg>
      maplowhearing.com
    </li>
  </ul>

  <address class="address">
    87 W. Linden Ave.<br>Alder Falls, OH 43910
  </address>

  <svg class="card-bands" viewBox="0 0 600 8" preserveAspectRatio="none" aria-hidden="true">
    <polygon points="0,0 376,0 372,8 0,8" fill="var(--brand-green)"/>
    <polygon points="379,0 600,0 600,8 375,8" fill="var(--card-black)"/>
  </svg>
</section>

<section class="card card-back" aria-label="Business card back">
  <div class="brand-name"><span class="brand-dot"></span>MAPLOW HEARING CENTER</div>
  <p class="site-url">www.<span class="accent">maplowhearing</span>.com</p>
</section>

</body>
</html>
```